Membership Card Design

I need a basic membership card...it will entitle the customer to free entry to forthcoming promotions.
The business is called STARLANE PLAY and is a amusement arcade located in N Ireland.
I require .....
STARLANE PLAY MEMBER...across top of card in logo format.
Next line....this card entitles the holder free entry to forthcoming STARLANE EVENTS....
Then next line....customer name( space to write their name )
Next line.....customer mobile number ( space to write number )
On rear of card....logo/picture & STARLANE PLAY MEMBER written on back.

Industry/Entity Type

Business

Contact Information for Business Card

STARLANE PLAY
MEMBERSHIP CARD

```html
<!DOCTYPE html>
<html lang="en">
<head>
<meta charset="utf-8">
<title>STARLANE PLAY Member Card</title>
<link href="https://fonts.googleapis.com/css2?family=Tinos:wght@400&display=swap" rel="stylesheet">
<style>
  :root {
    --card-black: #000000;
    --card-white: #ffffff;
    --art-light: #f2f2f2;
    --art-mid: #bdbdbd;
  }
  html, body {
    margin: 0;
    padding: 0;
    width: 1200px;
    height: 791px;
    overflow: hidden;
    background: var(--card-black);
  }
  .member-card {
    position: relative;
    width: 1200px;
    height: 791px;
    background: var(--card-black);
    color: var(--card-white);
    font-family: "Tinos", "Times New Roman", serif;
  }
  .card-title {
    position: absolute;
    left: 66px;
    width: 1068px;
    top: 52px;
    margin: 0;
    font-size: 76px;
    font-weight: 400;
    line-height: 1;
    text-align: center;
    white-space: nowrap;
  }
  .title-rule {
    position: absolute;
    left: 66px;
    top: 141px;
    width: 1068px;
    height: 3px;
    background: var(--card-white);
  }
  .entitlement {
    position: absolute;
    right: 74px;
    top: 166px;
    margin: 0;
    font-size: 39px;
    line-height: 52px;
    text-align: right;
    white-space: nowrap;
  }
  .entitlement .event-name {
    display: block;
  }
  .art-cards,
  .art-dice {
    position: absolute;
    background: linear-gradient(160deg, var(--art-light), var(--art-mid));
  }
  .art-cards {
    left: 125px;
    top: 240px;
    width: 449px;
    height: 314px;
  }
  .art-dice {
    left: 664px;
    top: 303px;
    width: 410px;
    height: 240px;
  }
  .write-in {
    position: absolute;
    left: 0;
    width: 1200px;
    height: 65px;
    background: var(--card-white);
    color: var(--card-black);
    font-size: 38px;
    line-height: 65px;
    box-sizing: border-box;
    padding-left: 66px;
    white-space: nowrap;
  }
  .write-in--name { top: 578px; }
  .write-in--phone { top: 661px; }
</style>
</head>
<body>
  <main class="member-card">
    <h1 class="card-title">STARLANE PLAY MEMBER</h1>
    <div class="title-rule"></div>
    <p class="entitlement">This card entitles the holder FREE entry to forthcoming
      <span class="event-name">STARLANE EVENTS</span></p>
    <div class="art-cards" role="img" aria-label="Fanned playing cards: ace, jack, king and queen of diamonds"></div>
    <div class="art-dice" role="img" aria-label="Pair of white dice"></div>
    <div class="write-in write-in--name">Customer name:</div>
    <div class="write-in write-in--phone">Customer mobile phone number:</div>
  </main>
</body>
</html>
```